Korvane Systems Website

Website design for our company: Korvane Systems.
The website should look fresh and IT focused. Please have a look at http://www.korvanesystems.example.au/ for our current design. We want something fresh and new, professional looking, in WordPress so we can easily make changes.

Industry/Entity Type

It Company

```html
<!DOCTYPE html>
<html lang="en">
<head>
<meta charset="utf-8">
<title>Korvane Systems — IT Services</title>
<link href="https://fonts.googleapis.com/css2?family=Questrial&family=Open+Sans:wght@400;600&display=swap" rel="stylesheet">
<style>
:root{
  --green:#0aa94f;
  --green-dark:#078a3f;
  --blue:#1a74bd;
  --blue-btn:#1473c4;
  --sky:#a9ccee;
  --ink:#333;
  --muted:#666;
  --grey-bg:#ebebeb;
  --line:#d9d9d9;
  --footer:#4a4a4a;
  --footer-top:#3e3e3e;
  --white:#fff;
}
*{box-sizing:border-box;margin:0;padding:0}
html,body{width:1200px;height:2639px;overflow:hidden}
body{position:relative;background:var(--white);font-family:"Open Sans",sans-serif;color:var(--ink)}
.abs{position:absolute}
.head{font-family:"Questrial",sans-serif}

/* header */
.topline{left:0;top:0;width:1200px;height:5px;background:var(--green)}
.header{left:0;top:5px;width:1200px;height:143px;background:linear-gradient(#fafafa,#e6e6e6);border-bottom:3px solid #d4d4d4}
.brand{left:84px;top:0;width:162px;height:148px;background:var(--green);border-bottom:5px solid var(--blue);display:flex;flex-direction:column;align-items:center;justify-content:center;gap:10px}
.brand-dot{width:34px;height:34px;border-radius:50%;background:var(--white)}
.brand-name{font-family:"Questrial",sans-serif;color:var(--white);font-size:19px;text-align:center;line-height:1.2}
.nav{left:350px;top:68px;display:flex;font-family:"Questrial",sans-serif;font-size:14px;letter-spacing:.5px;color:#444}
.nav span{margin-right:43px}

/* hero */
.hero{left:0;top:148px;width:1200px;height:486px;background:var(--sky)}
.hero-photo{left:0;top:148px;width:704px;height:486px;background:radial-gradient(circle at 45% 45%,#6fb7e8 0,#2d5f94 35%,#1c2d46 75%)}
.hero-title{left:714px;top:202px;font-size:33px;color:var(--blue)}
.hero-sub{left:714px;top:248px;width:440px;font-size:19px;line-height:26px;color:#1d2b3a}
.checks{left:720px;top:326px;list-style:none;font-size:17px;color:#1d2b3a}
.checks li{display:flex;align-items:flex-start;gap:14px;margin-bottom:13px;line-height:25px}
.checks svg{flex:none;margin-top:2px}
.lower-bg{left:0;top:634px;width:1200px;height:628px;background:var(--grey-bg)}

/* service cards */
.cards{left:37px;top:567px;width:1121px;height:255px;display:flex;background:linear-gradient(#fff,#e9e9e9);border:1px solid #cfcfcf;box-shadow:0 8px 12px rgba(0,0,0,.12)}
.card{position:relative;height:100%;border-right:1px solid #d2d2d2}
.card:last-child{border-right:0}
.card-icon{position:absolute;left:24px;top:54px}
.card-title{position:absolute;left:124px;top:52px;font-family:"Questrial",sans-serif;font-size:14px;letter-spacing:.5px;color:#222}
.card-text{position:absolute;left:124px;top:78px;width:250px;font-size:11.5px;letter-spacing:.3px;line-height:23px;color:#444}
.card-btn{position:absolute;left:126px;top:183px;width:106px;height:26px;background:var(--green);color:var(--white);font-size:11px;text-align:center;line-height:26px}
.card-btn.blue{background:var(--blue-btn)}

/* welcome */
.screen-frame{left:93px;top:889px;width:357px;height:224px;background:#1b1b1b;border-radius:6px}
.screen-photo{left:109px;top:904px;width:325px;height:188px;background:linear-gradient(135deg,#d9dee4,#9fb1c3 55%,#5e7288)}
.monitor-chin{left:93px;top:1113px;width:357px;height:22px;background:linear-gradient(#e6e6e6,#bdbdbd);border-radius:0 0 6px 6px}
.monitor-neck{left:232px;top:1135px;width:80px;height:28px;background:linear-gradient(#cfcfcf,#a9a9a9)}
.monitor-base{left:196px;top:1160px;width:152px;height:14px;background:#bfbfbf;border-radius:50%}
.welcome-title{left:505px;top:890px;font-size:25px;color:var(--blue)}
.welcome-rule{left:505px;top:935px;width:604px;height:1px;background:#d0d0d0}
.welcome-body{left:507px;top:955px;width:580px;font-size:15.5px;letter-spacing:.3px;line-height:22px;color:#444}
.welcome-body p{margin-bottom:22px}

/* how it works */
.how-title{left:67px;top:1329px;font-size:24px;color:var(--blue)}
.how-title em{font-style:normal;color:var(--green)}
.how-rule{left:56px;top:1385px;width:1109px;height:1px;background:var(--line)}
.step{left:78px;width:570px;height:140px}
.step-icon{position:absolute;left:0;top:0;width:100px;height:88px;background:linear-gradient(#fff,#ececec);border:1px solid #d6d6d6;box-shadow:0 3px 4px rgba(0,0,0,.12);display:flex;align-items:center;justify-content:center}
.step-title{position:absolute;left:119px;top:0;font-family:"Questrial",sans-serif;font-size:15px;letter-spacing:.5px;color:#222}
.step-text{position:absolute;left:119px;top:24px;width:450px;height:66px;overflow:hidden;font-size:14px;letter-spacing:.4px;line-height:22px;color:#555}
.step-more{position:absolute;left:119px;top:94px;font-size:12px;color:var(--blue)}

/* quote form */
.quote{left:739px;top:1429px;width:406px;height:530px;background:#f0f0f0;border:1px solid #d5d5d5}
.quote-head{left:732px;top:1440px;width:420px;height:52px;background:linear-gradient(#27c06a,#08973f);color:var(--white);font-family:"Questrial",sans-serif;font-size:21px;letter-spacing:1px;text-align:center;line-height:52px;border-radius:4px 4px 0 0;box-shadow:0 3px 4px rgba(0,0,0,.2)}
.field{left:762px;width:359px;height:49px;background:var(--white);border:2px solid #cfcfcf;font-size:20px;letter-spacing:1px;color:#8a8a8a;padding:10px 18px}
.qbtn{top:1866px;width:160px;height:38px;color:var(--white);font-size:15px;text-align:center;line-height:38px;border-radius:2px}
.qbtn.send{left:773px;background:linear-gradient(#19b85c,#078a3f)}
.qbtn.reset{left:950px;background:linear-gradient(#1e86d6,#0f62aa)}

/* partners */
.partners{left:0;top:2068px;width:1200px;height:150px;background:#efefef}
.partner{background:#b9b9b9}

/* footer */
.footer-top{left:0;top:2218px;width:1200px;height:62px;background:var(--footer-top)}
.footer{left:0;top:2280px;width:1200px;height:318px;background:var(--footer)}
.fcol-title{top:2321px;font-family:"Questrial",sans-serif;font-size:17px;letter-spacing:.5px;color:var(--white)}
.flinks{top:2380px;width:176px;list-style:none;font-size:15px;letter-spacing:.5px;color:var(--white)}
.flinks li{height:35px;line-height:34px;border-bottom:1px solid #5c5c5c}
.flinks li::before{content:"›";font-weight:600;margin-right:6px}
.contact-line{left:648px;width:240px;white-space:nowrap;font-size:15px;letter-spacing:.5px;color:var(--white);display:flex;align-items:center;gap:8px}
.social{top:2446px;width:26px;height:26px;border-radius:50%;background:var(--white)}
.news-note{left:905px;top:2384px;font-size:13px;color:var(--white)}
.news-input{left:905px;top:2413px;width:132px;height:32px;background:var(--white);font-size:12px;color:#777;padding:7px 8px}
.news-send{left:1037px;top:2413px;width:53px;height:32px;background:var(--green);color:var(--white);font-size:12px;text-align:center;line-height:32px}
.bottom{left:0;top:2598px;width:1200px;height:41px;background:var(--green);color:var(--white);font-size:12px;line-height:41px}
.bottom .copy{position:absolute;left:128px}
.bottom .links{position:absolute;right:107px}
</style>
</head>
<body>

<div class="abs topline"></div>
<header class="abs header"></header>
<div class="abs brand">
  <div class="brand-dot"></div>
  <div class="brand-name">Korvane Systems</div>
</div>
<nav class="abs nav">
  <span>HOME</span><span>ABOUT US</span><span>SERVICES</span><span>CLIENTS</span><span>SUPPORTS</span><span>TESTIMONIALS</span><span style="margin-right:0">CONTACT US</span>
</nav>

<section class="abs hero"></section>
<div class="abs hero-photo" role="img" aria-label="Businessman holding a glowing globe of connected devices, laptops, tablets and phones"></div>
<h1 class="abs head hero-title" style="font-weight:400">Heading title goes here</h1>
<p class="abs hero-sub">Lorem ipsum dolor sit amet consecto tetur adipiscing elit consectur sample.</p>
<ul class="abs checks">
  <li><svg width="22" height="22" viewBox="0 0 22 22"><rect x="1" y="3" width="17" height="17" fill="#fff" stroke="#1a74bd" stroke-width="2"/><path d="M5 11l4 4 11-13" fill="none" stroke="#1a74bd" stroke-width="3"/></svg>Auris at ligula ac lectus dictum sollicitudin.</li>
  <li><svg width="22" height="22" viewBox="0 0 22 22"><rect x="1" y="3" width="17" height="17" fill="#fff" stroke="#1a74bd" stroke-width="2"/><path d="M5 11l4 4 11-13" fill="none" stroke="#1a74bd" stroke-width="3"/></svg>Lorem ipsum dummy text only</li>
  <li><svg width="22" height="22" viewBox="0 0 22 22"><rect x="1" y="3" width="17" height="17" fill="#fff" stroke="#1a74bd" stroke-width="2"/><path d="M5 11l4 4 11-13" fill="none" stroke="#1a74bd" stroke-width="3"/></svg>Sample text goes here with second<br>line sentence sample</li>
</ul>

<div class="abs lower-bg"></div>

<div class="abs cards">
  <div class="card" style="width:355px">
    <svg class="card-icon" width="80" height="80" viewBox="0 0 80 80">
      <g stroke="#0aa94f" stroke-width="4"><line x1="40" y1="40" x2="40" y2="10"/><line x1="40" y1="40" x2="10" y2="40"/><line x1="40" y1="40" x2="70" y2="40"/><line x1="40" y1="40" x2="20" y2="68"/><line x1="40" y1="40" x2="60" y2="68"/></g>
      <circle cx="40" cy="40" r="13" fill="#0aa94f"/><circle cx="40" cy="10" r="7" fill="#1a74bd"/><circle cx="10" cy="40" r="7" fill="#0aa94f"/><circle cx="70" cy="40" r="7" fill="#0aa94f"/><circle cx="20" cy="68" r="7" fill="#1a74bd"/><circle cx="60" cy="68" r="7" fill="#1a74bd"/>
    </svg>
    <div class="card-title">NETWORK SERVICES</div>
    <div class="card-text">- Virtual Private Networks (VPN)<br>- Local Area Networks (LAN)<br>- Wide Area Networks (WAN)<br>- Inter office/ Intranet networks</div>
    <div class="card-btn">Read more ››</div>
  </div>
  <div class="card" style="width:389px">
    <svg class="card-icon" style="left:14px" width="90" height="80" viewBox="0 0 90 80">
      <path d="M18 50a16 16 0 0 1 4-31 22 22 0 0 1 42 4 14 14 0 0 1 6 27z" fill="#0aa94f"/>
      <g fill="#1a74bd"><rect x="28" y="36" width="12" height="38"/><rect x="43" y="32" width="12" height="42"/><rect x="58" y="36" width="12" height="38"/></g>
      <g stroke="#fff" stroke-width="2"><line x1="30" y1="46" x2="38" y2="46"/><line x1="45" y1="42" x2="53" y2="42"/><line x1="60" y1="46" x2="68" y2="46"/></g>
    </svg>
    <div class="card-title" style="left:120px">SERVER SERVICES</div>
    <div class="card-text" style="left:120px">We specialise in building, installing and managing customised servers for businesses of all sizes. Servers can be managed at your premises or ours.</div>
    <div class="card-btn blue" style="left:120px">Read more ››</div>
  </div>
  <div class="card" style="width:377px">
    <svg class="card-icon" width="70" height="84" viewBox="0 0 70 84">
      <path d="M14 38V26a21 21 0 0 1 42 0v12" fill="none" stroke="#1a74bd" stroke-width="9"/>
      <rect x="4" y="36" width="62" height="46" fill="#0aa94f"/>
      <circle cx="35" cy="54" r="7" fill="#fff"/><rect x="32" y="56" width="6" height="14" fill="#fff"/>
    </svg>
    <div class="card-title" style="left:115px">SECURITY SERVICES</div>
    <div class="card-text" style="left:115px;width:245px">Security is a major consideration when utilising most Information Technology devices. With the increasing use of all types of networks, security threats are</div>
    <div class="card-btn" style="left:120px">Read more ››</div>
  </div>
</div>

<div class="abs screen-frame"></div>
<div class="abs screen-photo" role="img" aria-label="Smiling team of business people standing together"></div>
<div class="abs monitor-chin"></div>
<div class="abs monitor-neck"></div>
<div class="abs monitor-base"></div>
<h2 class="abs head welcome-title" style="font-weight:400">Welcome to Korvane Systems</h2>
<div class="abs welcome-rule"></div>
<div class="abs welcome-body">
  <p>Korvane Systems is an Adelaide based company with a single objective - to excel in the support and service of all computer and IT needs.</p>
  <p>We provide a high level of consulting services using the most experienced engineers at a reasonable and fair price. We believe in using a Business Value approach to every aspect of computer consulting to provide our clients with the most cost effective solutions.</p>
  <p>We strongly believe that we are in business with our clients. Each thing we do must be measured against our clients' business objectives. At the end of the day our client's success is our success.</p>
</div>

<h2 class="abs head how-title" style="font-weight:400">How our <em>Services</em> work</h2>
<div class="abs how-rule"></div>

<div class="abs step" style="top:1436px">
  <div class="step-icon"><svg width="44" height="40" viewBox="0 0 44 40" fill="#0aa94f"><circle cx="10" cy="8" r="5"/><circle cx="22" cy="6" r="6"/><circle cx="34" cy="8" r="5"/><rect x="4" y="15" width="12" height="20" rx="3"/><rect x="15" y="14" width="14" height="24" rx="3"/><rect x="28" y="15" width="12" height="20" rx="3"/></svg></div>
  <div class="step-title">COMPLETE IT OUTSOURCING:</div>
  <div class="step-text">Provides a complete set of IT services, including all IT system planning, purchasing, implementation, consultation, and monitoring. This service is suitable when there is a lack of an IT</div>
  <div class="step-more">Read more →</div>
</div>
<div class="abs step" style="top:1586px">
  <div class="step-icon"><svg width="24" height="44" viewBox="0 0 24 44" fill="#0aa94f"><circle cx="12" cy="7" r="7"/><rect x="2" y="16" width="20" height="28" rx="4"/></svg></div>
  <div class="step-title">SINGLE ITEM IT OUTSOURCING SERVICE:</div>
  <div class="step-text">Perhaps your company has a few IT personnel, dealing with the scope of IT issues from daily administration and maintenance, to large or diverse difficulties. You could hand over</div>
  <div class="step-more">Read more →</div>
</div>
<div class="abs step" style="top:1737px">
  <div class="step-icon"><svg width="40" height="40" viewBox="0 0 40 40"><g stroke="#0aa94f" stroke-width="7" stroke-linecap="round"><line x1="8" y1="32" x2="32" y2="8"/><line x1="8" y1="8" x2="32" y2="32"/></g><circle cx="32" cy="8" r="7" fill="#0aa94f"/></svg></div>
  <div class="step-title">MAINTENANCE OUTSOURCING:</div>
  <div class="step-text">For those with an established IT system and limited routine work, if you require handy maintenance service when experiencing an unbearably busy time, you will enjoy our service via</div>
  <div class="step-more">Read more →</div>
</div>
<div class="abs step" style="top:1888px">
  <div class="step-icon"><svg width="44" height="44" viewBox="0 0 44 44" fill="#0aa94f"><ellipse cx="18" cy="8" rx="14" ry="5"/><rect x="4" y="12" width="28" height="8" rx="3"/><rect x="4" y="22" width="28" height="8" rx="3"/><rect x="4" y="32" width="28" height="8" rx="3"/><circle cx="34" cy="34" r="9"/><path d="M34 29v10M29 34h10" stroke="#fff" stroke-width="3"/></svg></div>
  <div class="step-title">INFORMATION TECHNOLOGY CONSULTATION:</div>
  <div class="step-text">The aim is to help our client find the right price, based on comparison and our accurate understanding of the IT professional frontier technology.</div>
  <div class="step-more">Read more →</div>
</div>

<div class="abs quote"></div>
<div class="abs quote-head">GET A FREE QUOTE</div>
<div class="abs field" style="top:1508px">Firstname</div>
<div class="abs field" style="top:1575px">Email Address</div>
<div class="abs field" style="top:1642px">Contact Number</div>
<div class="abs field" style="top:1709px;height:127px">Message</div>
<div class="abs qbtn send">Send Quote ››</div>
<div class="abs qbtn reset">Reset Form</div>

<div class="abs partners"></div>
<div class="abs partner" style="left:170px;top:2108px;width:104px;height:68px;border-radius:50%"></div>
<div class="abs partner" style="left:318px;top:2124px;width:148px;height:38px;border-radius:19px"></div>
<div class="abs partner" style="left:534px;top:2130px;width:118px;height:26px"></div>
<div class="abs partner" style="left:706px;top:2130px;width:138px;height:26px"></div>
<div class="abs partner" style="left:920px;top:2108px;width:70px;height:70px;border-radius:50%"></div>

<div class="abs footer-top"></div>
<footer class="abs footer"></footer>
<div class="abs fcol-title" style="left:132px">Product Info</div>
<ul class="abs flinks" style="left:124px"><li>Sublink here</li><li>Sublink here</li><li>Sublink here</li><li>Sublink here</li></ul>
<div class="abs fcol-title" style="left:378px">Additional Info</div>
<ul class="abs flinks" style="left:370px;width:186px"><li>F.A.Q</li><li>Terms &amp; Usage</li><li>Privacy Policy</li><li style="border:0">Sitemap</li></ul>
<div class="abs fcol-title" style="left:644px">Contact us</div>
<div class="abs contact-line" style="top:2383px"><svg width="16" height="12" viewBox="0 0 16 12"><rect width="16" height="12" fill="#fff"/><path d="M0 0l8 7 8-7" fill="none" stroke="#4a4a4a" stroke-width="1.5"/></svg>office@korvane.example</div>
<div class="abs contact-line" style="top:2413px"><svg width="16" height="12" viewBox="0 0 16 12" fill="#fff"><path d="M1 4c3-4 11-4 14 0l-3 2-2-2H6L4 6z"/><rect x="3" y="6" width="10" height="6" rx="1"/></svg>02-5550-187</div>
<div class="abs social" style="left:648px"></div>
<div class="abs social" style="left:684px"></div>
<div class="abs social" style="left:720px"></div>
<div class="abs fcol-title" style="left:910px">Newsletter Signup</div>
<div class="abs news-note">Subscribe to get updates</div>
<div class="abs news-input">Email address</div>
<div class="abs news-send">SEND</div>

<div class="abs bottom">
  <span class="copy">Copyright © 2014 Korvane Systems</span>
  <span class="links">FAQ &nbsp;·&nbsp; Sitemap &nbsp;·&nbsp; Privacy Policy</span>
</div>

</body>
</html>
```